Postcard Design

Law office.
Details are on the attached pdf file:
NOTE: the following items are to be changed, as follows:
1. price is 799
2. delete "Expires 2-8-13"
3. make "Nevada County's..." into "Northern California's ... "
4. Someplace where it fits nicely, add "Fast, Easy, Done!"
5. Delete "no obligation first visit"
6. That attached pdf was a successful ad so I want to maintain that look GENERALLY, but I'm not stuck on anything in particular. Some freedom to play with it for a perfect ad.
7. I'll attach the revised picture and the logo.

```html
<!DOCTYPE html>
<html lang="en">
<head>
<meta charset="utf-8">
<title>Moreno Law – Estate Plans Postcard</title>
<link rel="stylesheet" href="https://fonts.googleapis.com/css2?family=Crimson+Text:wght@400;700&family=Open+Sans:ital,wght@0,400;1,400;1,700&family=Oswald:wght@700&display=swap">
<style>
  :root {
    --brand-blue: #1767a0;
    --brand-blue-dark: #0f5688;
    --charcoal: #474747;
    --ink: #1e1e1e;
    --text-grey: #4f4f4f;
    --paper: #ffffff;
    --paper-shade: #e6e6e6;
    --rule-grey: #bdbdbd;
    --stage: #d9d9d9;
  }
  * { margin: 0; padding: 0; box-sizing: border-box; }
  html, body {
    width: 1200px; height: 825px; overflow: hidden;
    background: var(--stage);
  }
  .postcard {
    position: absolute; left: 27px; top: 0;
    width: 967px; height: 695px;
    transform: scale(1.187); transform-origin: 0 0;
    background: linear-gradient(160deg, var(--paper) 0%, #f4f4f4 40%, var(--paper-shade) 100%);
    overflow: hidden;
    font-family: "Open Sans", Arial, sans-serif;
  }
  .postcard__frame { position: absolute; inset: 0; }
  .headline {
    position: absolute; left: 0; top: 27px; width: 860px; height: 70px;
    display: flex; align-items: center; justify-content: center;
    font-family: "Crimson Text", Georgia, serif; font-weight: 700;
    font-size: 38px; color: var(--paper); letter-spacing: .3px;
  }
  .services {
    position: absolute; left: 0; top: 118px; width: 870px; text-align: center;
    font-style: italic; font-size: 33px; color: var(--ink);
  }
  .price {
    position: absolute; left: 88px; top: 170px;
    font-family: "Oswald", Impact, sans-serif; font-weight: 700;
    font-size: 112px; line-height: 1; color: var(--brand-blue);
    letter-spacing: -1px;
  }
  .price-divider {
    position: absolute; left: 366px; top: 196px; width: 2px; height: 92px;
    background: var(--ink);
  }
  .value {
    position: absolute; left: 404px; top: 182px;
    font-family: "Oswald", Impact, sans-serif; font-weight: 700;
    font-size: 44px; line-height: 1.2; color: var(--brand-blue);
  }
  .tagline {
    position: absolute; left: 436px; top: 238px;
    font-style: italic; font-size: 35px; color: var(--ink);
  }
  .promise {
    position: absolute; left: 45px; top: 314px;
    font-family: "Crimson Text", Georgia, serif; font-weight: 700;
    font-size: 37px; color: var(--text-grey);
  }
  .call-pill {
    position: absolute; left: 532px; top: 319px; width: 312px; height: 42px;
    border-radius: 21px; background: var(--brand-blue);
    border: 3px solid var(--paper); box-shadow: 0 0 0 1px #c9c9c9;
    display: flex; align-items: center; justify-content: center;
    font-style: italic; font-size: 23px; color: var(--paper);
  }
  .portrait {
    position: absolute; left: 42px; top: 380px; width: 190px; height: 238px;
    background: #d8d8d8; padding: 11px;
    box-shadow: 0 6px 10px rgba(0,0,0,.15);
  }
  .portrait__fill {
    width: 100%; height: 100%;
    background: linear-gradient(180deg, #8d9397 0%, #6e7478 45%, #2a2c2e 100%);
  }
  .office {
    position: absolute; left: 270px; top: 400px; width: 420px; text-align: center;
    font-family: "Crimson Text", Georgia, serif; color: var(--ink);
  }
  .office__label { font-size: 25px; line-height: 1.2; }
  .office__name { font-size: 38px; line-height: 1.25; color: var(--brand-blue); letter-spacing: .5px; }
  .office__phone { font-size: 27px; font-weight: 700; line-height: 1.35; }
  .office__web { font-size: 21px; line-height: 1.9; }
  .office__notary {
    font-family: "Open Sans", Arial, sans-serif; font-style: italic; font-weight: 700;
    font-size: 28px; color: var(--brand-blue); line-height: 1.35;
  }
  .brand-mark {
    position: absolute; left: 719px; top: 417px; width: 138px; height: 170px;
    border: 3px solid var(--ink); background: var(--paper);
    display: flex; align-items: center; justify-content: center; text-align: center;
    font-family: "Crimson Text", Georgia, serif; font-size: 30px; line-height: 1.1;
    color: var(--ink);
  }
  .brand-since {
    position: absolute; left: 700px; top: 598px; width: 176px; text-align: center;
    font-size: 14px; line-height: 1.3; color: var(--ink);
  }
</style>
</head>
<body>
  <main class="postcard">
    <svg class="postcard__frame" width="967" height="695" viewBox="0 0 967 695" aria-hidden="true">
      <rect x="0" y="22" width="900" height="6" fill="var(--rule-grey)"/>
      <rect x="0" y="28" width="900" height="70" fill="var(--brand-blue)"/>
      <rect x="0" y="662" width="900" height="33" fill="var(--brand-blue)"/>
      <path d="M880 0 C850 80 858 140 882 260 C905 380 870 520 860 695 L967 695 L967 0 Z" fill="var(--brand-blue)"/>
      <path d="M900 0 C870 80 878 140 902 260 C925 380 890 520 880 695 L967 695 L967 0 Z" fill="var(--paper)"/>
      <path d="M912 0 C882 80 890 140 914 260 C937 380 902 520 892 695 L967 695 L967 0 Z" fill="var(--charcoal)"/>
    </svg>

    <h1 class="headline">Northern California's Best in Estate Plans</h1>
    <p class="services">Living Trusts, Wills &amp; All Necessary Documents</p>
    <p class="price">$799</p>
    <span class="price-divider"></span>
    <p class="value">Over $2,000 value</p>
    <p class="tagline">Fast, Easy, Done!</p>
    <p class="promise">Protect Your Loved Ones!</p>
    <p class="call-pill">It’s Easy — Call Now!</p>

    <figure class="portrait">
      <div class="portrait__fill" role="img" aria-label="Portrait photo of the attorney in a dark suit and tie"></div>
    </figure>

    <section class="office">
      <p class="office__label">THE LAW OFFICE OF</p>
      <p class="office__name">DANIEL R. MORENO</p>
      <p class="office__phone">Call at - 555-0142</p>
      <p class="office__web">Check me out at: www.DanielMoreno.com</p>
      <p class="office__notary">Free Notarization</p>
    </section>

    <div class="brand-mark">Moreno<br>Law</div>
    <p class="brand-since">Thousands Served<br>Since 1998</p>
  </main>
</body>
</html>
```